Falcrest security business card

Looking for a business card for my security company

Target Market(s)

Security

Industry/Entity Type

Security

Contact Information for Business Card

Name - Gil Marston. Title - General manager - direct 314 862.4490 website www. falcrestsecurityservices.example email - gil@ falcrestsecurityservices.example

Requirements
Must have
• Logo attached

```html
<!DOCTYPE html>
<html lang="en">
<head>
<meta charset="utf-8">
<title>Falcrest Security Services – Business Card</title>
<link rel="stylesheet" href="https://fonts.googleapis.com/css2?family=Michroma&family=Roboto:wght@400;700;900&display=swap">
<style>
  :root {
    --canvas: #ffffff;
    --card-black: #0b0b0b;
    --card-white: #ffffff;
    --gold: #d9a93f;
    --gold-light: #f0cf7a;
    --ink: #111111;
    --ink-soft: #4a4a4a;
    --rule: #c9c9c9;
    --circuit: #2a2a2a;
  }
  * { margin: 0; padding: 0; box-sizing: border-box; }
  html, body {
    width: 1200px; height: 2400px; overflow: hidden;
    background: var(--canvas);
  }
  .sheet {
    position: relative; width: 1200px; height: 2400px;
  }
  .card {
    position: absolute; left: 95px; width: 1010px; height: 576px;
    box-shadow: 0 6px 10px rgba(0,0,0,.35);
    overflow: hidden;
  }
  /* Front */
  .card--front { top: 600px; background: var(--card-black); }
  .front__circuit {
    position: absolute; top: 120px; height: 330px; width: 380px;
  }
  .front__circuit--left {
    left: 50px;
    background: radial-gradient(ellipse at 60% 50%, var(--circuit), transparent 70%);
  }
  .front__circuit--right {
    right: 50px;
    background: radial-gradient(ellipse at 40% 50%, var(--circuit), transparent 70%);
  }
  .front__brand {
    position: absolute; left: 0; right: 0; top: 228px;
    display: flex; align-items: center; justify-content: center; gap: 22px;
  }
  .front__mark {
    width: 34px; height: 34px; background: var(--gold);
  }
  .front__name {
    font-family: "Michroma", sans-serif; font-size: 62px; letter-spacing: 4px;
    color: var(--gold); line-height: 1;
  }
  .front__url {
    position: absolute; left: 0; right: 0; top: 496px; text-align: center;
    font-family: "Michroma", sans-serif; font-size: 17px; letter-spacing: 3px;
    color: #ffffff;
  }
  .front__url .domain { color: var(--gold); }

  /* Back */
  .card--back { top: 1222px; background: var(--card-white); }
  .back__band {
    position: absolute; top: 0; left: 0; right: 0; height: 42px;
    background: var(--card-black);
  }
  .back__brand {
    position: absolute; left: 78px; top: 150px;
    display: flex; align-items: center; gap: 16px;
  }
  .back__mark { width: 30px; height: 30px; background: var(--ink); }
  .back__name {
    font-family: "Roboto", sans-serif; font-weight: 900; font-size: 62px;
    letter-spacing: 1px; color: var(--ink); line-height: 1;
  }
  .person {
    position: absolute; right: 82px; top: 238px; text-align: right;
    font-family: "Roboto", sans-serif;
  }
  .person__name {
    font-weight: 700; font-size: 46px; color: var(--ink); line-height: 1;
    letter-spacing: .5px;
  }
  .person__title {
    font-weight: 400; font-size: 27px; color: var(--ink-soft); margin-top: 6px;
  }
  .back__rule {
    position: absolute; left: 85px; right: 82px; top: 359px;
    height: 2px; background: var(--rule);
  }
  .contact {
    position: absolute; right: 82px; top: 398px;
    list-style: none; font-family: "Roboto", sans-serif;
  }
  .contact__item {
    display: flex; align-items: center; justify-content: flex-end;
    gap: 16px; height: 46px; font-size: 23px; color: var(--ink-soft);
  }
  .contact__item--phone { font-weight: 700; color: var(--ink); }
  .contact__icon { width: 28px; height: 28px; flex: none; }
</style>
</head>
<body>
<main class="sheet">

  <section class="card card--front" aria-label="Card front">
    <div class="front__circuit front__circuit--left" role="img" aria-label="Faint circuit-line decoration"></div>
    <div class="front__circuit front__circuit--right" role="img" aria-label="Faint circuit-line decoration"></div>
    <div class="front__brand">
      <span class="front__mark" aria-hidden="true"></span>
      <span class="front__name">FALCREST</span>
    </div>
    <p class="front__url">WWW.<span class="domain">FALCRESTSECURITYSERVICES</span>.EXAMPLE</p>
  </section>

  <section class="card card--back" aria-label="Card back">
    <div class="back__band"></div>
    <div class="back__brand">
      <span class="back__mark" aria-hidden="true"></span>
      <span class="back__name">FALCREST</span>
    </div>
    <div class="person">
      <p class="person__name">GIL MARSTON</p>
      <p class="person__title">General manager</p>
    </div>
    <div class="back__rule"></div>
    <ul class="contact">
      <li class="contact__item contact__item--phone">
        <span>314 862.4490</span>
        <svg class="contact__icon" viewBox="0 0 24 24" fill="none" stroke="#333" stroke-width="1.4" stroke-linejoin="round">
          <path d="M5 3h4l2 5-2.5 1.5a11 11 0 0 0 6 6L16 13l5 2v4a2 2 0 0 1-2 2A16 16 0 0 1 3 5a2 2 0 0 1 2-2z"/>
        </svg>
      </li>
      <li class="contact__item">
        <span>gil@ falcrestsecurityservices.example</span>
        <svg class="contact__icon" viewBox="0 0 24 24" fill="none" stroke="#333" stroke-width="1.4">
          <rect x="2.5" y="5" width="19" height="14"/>
          <path d="M2.5 5l9.5 8 9.5-8"/>
        </svg>
      </li>
      <li class="contact__item">
        <span>www.falcrestsecurityservices.example</span>
        <svg class="contact__icon" viewBox="0 0 24 24" fill="none" stroke="#222" stroke-width="1.6">
          <circle cx="12" cy="12" r="9.5"/>
          <ellipse cx="12" cy="12" rx="4" ry="9.5"/>
          <path d="M2.5 12h19M4 7h16M4 17h16"/>
        </svg>
      </li>
    </ul>
  </section>

</main>
</body>
</html>
```